Ironvale Shift Services

We are a underground coal mining labour hire company, needing a website that links into our online payroll (www.wagetrakker.com.au) and also need to have job applications page that is a preform with drop down menu,s with answers or check boxes. We would also need a 3 tier administration access for access to different files.
We are looking for an ongoing relationship with future app integration

Reason: There are a few more designs to come and I'm out at the mine for another week

Industry/Entity Type

Coal Mining

```html
<!DOCTYPE html>
<html lang="en">
<head>
<meta charset="utf-8">
<title>Ironvale Shift Services</title>
<link href="https://fonts.googleapis.com/css2?family=PT+Sans+Narrow:wght@400;700&family=PT+Sans:wght@400;700&family=Open+Sans:ital,wght@1,700&display=swap" rel="stylesheet">
<style>
:root{
  --bg-top:#1b1b1b;
  --bg-nav:#0c0c0c;
  --bg-content:#222;
  --bg-footer:#1a1a1a;
  --bg-bottom:#0b0b0b;
  --red:#d8321c;
  --text:#8a8a8a;
  --text-light:#cfcfcf;
  --heading:#e4e4e4;
  --muted:#6b6b6b;
  --divider:#3a3a3a;
}
*{margin:0;padding:0;box-sizing:border-box}
html,body{width:960px;height:1200px;overflow:hidden;background:var(--bg-top)}
body{position:relative;font-family:"PT Sans",Arial,sans-serif;color:var(--text);font-size:10.5px;line-height:14.5px}
.abs{position:absolute}

/* navigation */
.topbar{left:0;top:0;width:960px;height:55px;background:var(--bg-nav)}
.nav{left:88px;top:0;display:flex;height:47px;align-items:center;font-family:"PT Sans Narrow",sans-serif;font-weight:700;font-size:15px;text-transform:uppercase}
.nav a{color:#9a9a9a;text-decoration:none}
.nav .home{background:var(--red);color:#fff;height:47px;width:66px;display:flex;align-items:center;justify-content:center}
.nav .sep{width:1px;height:12px;background:#444;margin:0 26px}
.nav .sep.first{margin-left:10px}
.support{left:722px;top:13px;display:flex;align-items:center;gap:8px}
.support .lbl{font-family:"PT Sans Narrow",sans-serif;color:#aaa;font-size:12px;line-height:11px}
.support .num{font-family:"PT Sans Narrow",sans-serif;color:#eee;font-size:17px;line-height:16px;font-weight:700}

/* header */
.brand{left:88px;top:72px;display:flex;align-items:center;gap:12px}
.brand .dot{width:72px;height:72px;border-radius:50%;border:4px solid #8f8f8f}
.brand .name{font-family:"PT Sans",sans-serif;font-size:40px;color:#a9a9a9;font-weight:400}
.tagline{left:388px;top:92px;font-family:"Open Sans",sans-serif;font-style:italic;font-weight:700;font-size:16px;line-height:22px;color:#8c8c8c;text-transform:uppercase;letter-spacing:-.3px}

/* slider */
.feature-art{left:89px;top:167px;width:223px;height:400px;background:radial-gradient(circle at 50% 42%,#c8281a 0,#6e1610 38%,#0a0a0a 72%)}
.feature-art .caption{position:absolute;left:22px;top:233px;width:180px;background:#111;color:#eee;font-size:11px;text-align:center;padding:2px 0}
.slide-main{left:312px;top:167px;width:565px;height:253px;background:linear-gradient(180deg,#5a5a5a 0,#8e8e8e 45%,#b9b6b0 100%)}
.thumbs{left:312px;top:420px;width:565px;height:147px;background:#141414}
.thumb{position:absolute;top:17px;width:88px;height:120px;border:2px solid #2a2a2a}
.arrow{position:absolute;top:56px;width:26px;height:40px;background:#2b2b2b;display:flex;align-items:center;justify-content:center}

/* content */
.content{left:0;top:593px;width:960px;height:315px;background:var(--bg-content)}
.col{position:absolute;top:30px;width:210px}
.col h2{font-family:"PT Sans Narrow",sans-serif;font-size:16px;color:var(--heading);text-transform:uppercase;display:flex;align-items:center;gap:8px;margin-bottom:20px}
.col h2 svg{width:22px;height:22px}
.date{color:#ddd;font-weight:700;text-decoration:underline;font-size:10.5px;padding-left:10px;position:relative}
.date:before,.more-link:before{content:"";position:absolute;left:0;top:4px;border:3px solid transparent;border-left-color:#777}
.para{margin-bottom:40px}
.para u{color:#ccc}
.job{margin-bottom:16px;padding-left:12px;position:relative}
.job:before{content:"";position:absolute;left:0;top:3px;width:7px;height:7px;border:1px solid #888}
.job .place{color:var(--red);font-weight:700;text-decoration:underline}
.btn{display:inline-block;background:var(--red);color:#fff;font-size:10.5px;padding:4px 10px;border-bottom:2px solid #8e1f12}
.btn-pos{position:absolute;top:257px}

/* footer */
.footer{left:0;top:908px;width:960px;height:220px;background:var(--bg-footer)}
.fcol{position:absolute;top:32px}
.fcol h3{font-family:"PT Sans Narrow",sans-serif;font-size:16px;color:var(--heading);text-transform:uppercase;margin-bottom:22px}
.partner{position:relative;width:204px;height:117px;background:#2a2a2a;border:2px solid #3b3b3b;text-align:center;padding-top:24px}
.partner .t1{font-size:17px;color:#9a9a9a;line-height:22px}
.partner .t2{font-size:16px;color:#e8e8e8;line-height:26px;margin-top:4px}
.partner .btn{position:absolute;left:70px;bottom:-12px}
.office{line-height:16px;color:#9a9a9a;font-size:10.5px}
.office span{display:inline-block;width:54px}
.services li{list-style:none;color:#bdbdbd;font-weight:700;font-size:10.5px;margin-bottom:8px;padding-left:11px;position:relative}
.services li:before{content:"";position:absolute;left:0;top:4px;border:3px solid transparent;border-left-color:#777}

/* bottom */
.bottom{left:0;top:1128px;width:960px;height:72px;background:var(--bg-bottom)}
.copy{left:89px;top:38px;font-size:9.5px;color:var(--muted)}
.social{left:835px;top:16px;display:flex;gap:4px}
.social i{display:block;width:19px;height:19px;background:#555;border:1px solid #888}
.fnav{right:83px;top:40px;font-size:10px;color:#777}
.fnav a{color:#888;text-decoration:none}
.fnav a.cur{color:#ddd}
</style>
</head>
<body>

<header class="abs topbar"></header>
<nav class="abs nav">
  <a class="home" href="#">Home</a><span class="sep first"></span>
  <a href="#">About us</a><span class="sep"></span>
  <a href="#">Services</a><span class="sep"></span>
  <a href="#">Projects</a><span class="sep"></span>
  <a href="#">Solutions</a><span class="sep"></span>
  <a href="#">Contacts</a><span class="sep"></span>
</nav>
<div class="abs support">
  <svg width="26" height="26" viewBox="0 0 26 26"><circle cx="13" cy="13" r="10" fill="none" stroke="#888" stroke-width="3" stroke-dasharray="4 2.5"/></svg>
  <div><div class="lbl">24/7 SUPPORT CENTER:</div><div class="num">1-800-555-0142</div></div>
</div>

<div class="abs brand"><div class="dot"></div><div class="name">Ironvale</div></div>
<div class="abs tagline">We are professional<br>underground coal mining labour hire company</div>

<div class="abs feature-art" role="img" aria-label="Illustration of a miner in a hard hat with arms crossed over a red burst, Ironvale Shift Services">
  <div class="caption">Ironvale Shift Services</div>
</div>
<div class="abs slide-main" role="img" aria-label="Photo of tracked excavators working on a dusty mine site"></div>
<div class="abs thumbs">
  <div class="arrow" style="left:8px;border-radius:13px 0 0 13px"><svg width="6" height="8"><path d="M6 0L0 4L6 8Z" fill="#ddd"/></svg></div>
  <div class="thumb" role="img" aria-label="Thumbnail of excavator" style="left:30px;background:linear-gradient(#6a6a6a,#cfcfcf);border-color:#ddd"></div>
  <div class="thumb" role="img" aria-label="Thumbnail of haul truck" style="left:134px;background:linear-gradient(#3a3a3a,#1e1e1e)"></div>
  <div class="thumb" role="img" aria-label="Thumbnail of excavator arm" style="left:238px;background:linear-gradient(#4a4a4a,#2a2a2a)"></div>
  <div class="thumb" role="img" aria-label="Thumbnail of wheel loader" style="left:342px;background:linear-gradient(#555,#2e2e2e)"></div>
  <div class="thumb" role="img" aria-label="Thumbnail of shovel at dusk" style="left:446px;background:linear-gradient(#555,#1a1a1a)"></div>
  <div class="arrow" style="left:531px;border-radius:0 13px 13px 0"><svg width="6" height="8"><path d="M0 0L6 4L0 8Z" fill="#ddd"/></svg></div>
</div>

<section class="abs content">
  <div class="col" style="left:88px">
    <h2><svg viewBox="0 0 22 22"><circle cx="11" cy="11" r="8" fill="none" stroke="#bbb" stroke-width="4" stroke-dasharray="3 1.6"/><circle cx="11" cy="11" r="3" fill="#bbb"/></svg>News &amp; Events</h2>
    <div class="date">Fri, Jan. 20</div>
    <p class="para">Etum nam libero tempore, cum soluta nobis est eligendi omnis voluptas assmenda est, omnis doloresed quibusdam et aut officiis debitis aut necessitatibus saepe eveniet ut et voluptates</p>
    <div class="date">Wed, Dec. 05</div>
    <p>Nam libero tempore, cum soluta nobis est eligendi omnis voluptas assmenda est, omnis doloresedumquibusdam et aut officiis debitis aut</p>
    <a class="btn btn-pos" href="#" style="left:2px">View all</a>
  </div>
  <div class="col" style="left:380px">
    <h2><svg viewBox="0 0 22 22"><circle cx="11" cy="11" r="8" fill="none" stroke="#bbb" stroke-width="4" stroke-dasharray="3 1.6"/><circle cx="11" cy="11" r="3" fill="#bbb"/></svg>Welcome</h2>
    <p class="para">Arum nam libero tempore, cum soluta nobis est eligendi omnis voluptas assmenda est, omnis doloresed <u>quibusdam et aut officiis debitis</u> aut necessitatibus saepe eveniet ut et voluptates repudiandae sint et molestiae non recusandae.</p>
    <p>Arum nam libero tempore, cum soluta nobis est eligendi omnis voluptas assmenda est, omnis doloresed quibusdam et aut officiis debitis aut necessitatibus saepe eveniet ut et voluptates</p>
    <a class="btn btn-pos" href="#" style="left:1px">Read more</a>
  </div>
  <div class="col" style="left:673px">
    <h2><svg viewBox="0 0 22 22"><circle cx="11" cy="11" r="8" fill="none" stroke="#bbb" stroke-width="4" stroke-dasharray="3 1.6"/><circle cx="11" cy="11" r="3" fill="#bbb"/></svg>Latest jobs</h2>
    <div class="job"><div class="place">New York</div>repudiandae sint et moles mam libero temp cum soluta nobiest eligendi mnis volum</div>
    <div class="job"><div class="place">California</div>repudiandae sint et moles mam libero temp cum soluta nobiest eligendi mnis volum</div>
    <div class="job"><div class="place">Alaska</div>repudiandae sint et moles mam libero temp cum soluta nobiest eligendi mnis volum</div>
    <a class="btn btn-pos" href="#" style="left:1px">Read more</a>
  </div>
</section>

<footer class="abs footer">
  <div class="fcol" style="left:88px">
    <h3>Partners</h3>
    <div class="partner">
      <div class="t1">Easy Online Payroll</div>
      <div class="t2">wagetrakker.com.au</div>
      <a class="btn" href="#">Read more</a>
    </div>
  </div>
  <div class="fcol" style="left:380px">
    <h3>Central office</h3>
    <div class="office">
      412 Collier Row,<br>Brackenford, QN 48 Tr 21.<br>
      <span>Support:</span>+1 800 555 0181<br>
      <span>Local:</span>+1 800 555 0193<br>
      <span>FAX:</span>+1 800 555 0167<br>
      E-Mail: office@ironvale.example
    </div>
  </div>
  <div class="fcol" style="left:673px">
    <h3>Our services</h3>
    <ul class="services">
      <li>Clearing, grubbing, mulching</li>
      <li>Topsoil stripping</li>
      <li>Rock breaking/excavations</li>
      <li>Ground stabilisation</li>
      <li>Bulk earthworks</li>
    </ul>
  </div>
</footer>

<div class="abs bottom">
  <div class="abs copy">Mining Industry © 2010 | Privacy policy</div>
  <div class="abs social"><i></i><i></i></div>
  <div class="abs fnav"><a class="cur" href="#">Home</a> | <a href="#">About Us</a> | <a href="#">Services</a> | <a href="#">Projects</a> | <a href="#">Solutions</a> | <a href="#">Contacts</a></div>
</div>

</body>
</html>
```